Looking for updated Letterhead and Compliments Slips to go with our new updated logo. This stationary will be used for letters to suppliers and customers so needs to be practical while also quite classic.

We are an engineering company so needs to be clean and precise

Target Market(s)

SME'S and large automotive customers

Industry/Entity Type

Automotive

Font styles to use
Sans Serif

Colors
85acd3
0356a4
0792cd
33a6d7
85abd2
ffffff

Requirements
Must have
• Address details as below
• KT Fabrications Limited
• Hallmere Road
• Ashmere
• Westvale
• LP47 9XZ, UK
• Telephone: +44 (0)1632 960418
• Fax: +44 (0)1632 960733
• Email: sales@ktfabrications.example
• Web: www.ktfabrications.example
Nice to have
• Nice to have some element of being a British Manufacturer

```html
<!DOCTYPE html>
<html lang="en">
<head>
<meta charset="utf-8">
<title>KT Fabrications – Stationery</title>
<link rel="stylesheet" href="https://fonts.googleapis.com/css2?family=Montserrat:wght@600&family=Source+Sans+3:wght@400;600&display=swap">
<style>
  :root{
    --brand-blue:#0356a4;
    --brand-sky:#0792cd;
    --brand-light:#85acd3;
    --paper:#ffffff;
    --backdrop:#eef0f3;
    --text-grey:#5a5d63;
    --shadow:0 6px 18px rgba(0,0,0,.18);
  }
  *{box-sizing:border-box;margin:0;padding:0}
  html,body{width:999px;height:1200px;overflow:hidden}
  body{background:var(--backdrop);font-family:"Source Sans 3",Arial,sans-serif;position:relative}

  .sheet{position:absolute;background:var(--paper);box-shadow:var(--shadow);overflow:hidden}

  /* wordmark */
  .wordmark{display:flex;align-items:center;gap:10px;font-family:"Montserrat",Arial,sans-serif;font-weight:600;color:var(--brand-blue);letter-spacing:.28em;white-space:nowrap}
  .wordmark .dot{width:12px;height:12px;border-radius:50%;background:var(--brand-blue);flex:none}

  /* address block */
  .address{color:var(--text-grey);text-align:center;line-height:1.4;font-weight:400}
  .address .line{display:block;white-space:nowrap}
  .address .label{color:var(--brand-blue)}

  /* letterhead */
  .letterhead{left:40px;top:40px;width:560px;height:792px}
  .letterhead .header-rule{position:absolute;top:112px;height:5px;background:var(--brand-blue)}
  .letterhead .header-rule.left{left:0;width:160px}
  .letterhead .header-rule.right{right:0;width:160px}
  .letterhead .wordmark{position:absolute;top:100px;left:0;right:0;justify-content:center;font-size:15px}
  .letterhead .footer-rule{position:absolute;left:40px;right:0;bottom:86px;height:4px;background:var(--brand-blue)}
  .letterhead .footer-block{position:absolute;right:0;bottom:38px;width:110px;height:40px;background:var(--brand-blue)}
  .letterhead .address{position:absolute;left:40px;width:400px;bottom:30px;font-size:9px}

  /* compliments slip */
  .slip{left:40px;top:872px;width:560px;height:264px}
  .slip .band{position:absolute;left:0;top:0;width:100%;height:52px;background:var(--brand-blue)}
  .slip .band-rule{position:absolute;left:0;top:58px;width:100%;height:4px;background:var(--brand-blue)}
  .slip .band-rule.thin{top:66px;height:3px}
  .slip .wordmark{position:absolute;top:130px;left:0;right:0;justify-content:center;font-size:15px}
  .slip .address{position:absolute;left:0;right:0;bottom:22px;font-size:9.5px}

  /* business card */
  .card{left:640px;top:300px;width:320px;height:200px}
  .card .wordmark{position:absolute;top:64px;left:0;right:0;justify-content:center;font-size:11px;gap:7px}
  .card .wordmark .dot{width:9px;height:9px}
  .card .card-rule{position:absolute;left:0;right:0;top:128px;height:3px;background:var(--brand-blue)}
  .card .card-band{position:absolute;left:0;right:0;bottom:0;height:58px;background:var(--brand-blue)}
  .card .address{position:absolute;left:0;right:0;bottom:11px;font-size:7px;color:var(--paper)}
  .card .address .label{color:var(--paper)}
</style>
</head>
<body>

  <section class="sheet letterhead" aria-label="Letterhead">
    <div class="header-rule left"></div>
    <div class="wordmark"><span class="dot"></span>KT FABRICATIONS</div>
    <div class="header-rule right"></div>
    <div class="footer-rule"></div>
    <div class="footer-block"></div>
    <p class="address">
      <span class="line">Address details as below - KT Fabrications Limited&nbsp; Hallmere Road - Ashmere - Westvale</span>
      <span class="line">LP47 9XZ, UK - <span class="label">Telephone:</span> +44 (0)1632 960418 - <span class="label">Fax:</span> +44 (0)1632 960733</span>
      <span class="line"><span class="label">Email:</span> sales@ktfabrications.example - <span class="label">Web:</span> www.ktfabrications.example</span>
    </p>
  </section>

  <section class="sheet slip" aria-label="Compliments slip">
    <div class="band" role="img" aria-label="Blue header band with repeating brand pattern"></div>
    <div class="band-rule"></div>
    <div class="band-rule thin"></div>
    <div class="wordmark"><span class="dot"></span>KT FABRICATIONS</div>
    <p class="address">
      <span class="line">Address details as below - KT Fabrications Limited&nbsp; Hallmere Road - Ashmere - Westvale</span>
      <span class="line">LP47 9XZ, UK - <span class="label">Telephone:</span> +44 (0)1632 960418 - <span class="label">Fax:</span> +44 (0)1632 960733</span>
      <span class="line"><span class="label">Email:</span> sales@ktfabrications.example - <span class="label">Web:</span> www.ktfabrications.example</span>
    </p>
  </section>

  <section class="sheet card" aria-label="Business card">
    <div class="wordmark"><span class="dot"></span>KT FABRICATIONS</div>
    <div class="card-rule"></div>
    <div class="card-band"></div>
    <p class="address">
      <span class="line">Address details as below - KT Fabrications Limited&nbsp; Hallmere Road - Ashmere - Westvale</span>
      <span class="line">LP47 9XZ, UK - <span class="label">Telephone:</span> +44 (0)1632 960418 - <span class="label">Fax:</span> +44 (0)1632 960733</span>
      <span class="line"><span class="label">Email:</span> sales@ktfabrications.example - <span class="label">Web:</span> www.ktfabrications.example</span>
    </p>
  </section>

</body>
</html>
```